Bramwell Ridge Minerals

Looking for a cool, glossy business card...white with our logo on one side and then the a smaller version of the logo on the other side (top left hand corner) and then the name and position of the person next to it, and then the office address and email address on the bottom left hand corner and the phone numbers & email address on the bottom right hand corner. I have the logo already...can pass it on when you're ready.

```html
<!DOCTYPE html>
<html lang="en">
<head>
<meta charset="utf-8">
<title>Bramwell Ridge Minerals – Business Cards</title>
<link href="https://fonts.googleapis.com/css2?family=Cinzel:wght@600&family=Alegreya:wght@400;500&display=swap" rel="stylesheet">
<style>
  :root {
    --page-bg: #ecebe8;
    --card-bg: #fbfbfa;
    --card-edge: #d9d7d2;
    --navy: #1d3f7a;
    --red: #9e1c22;
    --red-dark: #7f1419;
    --blue-line: #2a5aa6;
    --ink: #3a3a3a;
    --ink-soft: #555;
    --band-text: #f3e4e0;
  }
  * { box-sizing: border-box; margin: 0; padding: 0; }
  html, body { width: 1200px; height: 1051px; overflow: hidden; }
  body {
    background: var(--page-bg);
    position: relative;
    font-family: "Alegreya", Georgia, serif;
    color: var(--ink);
  }
  .card {
    position: absolute;
    width: 442px;
    height: 266px;
    background: var(--card-bg);
    border: 1px solid var(--card-edge);
    box-shadow: 0 6px 18px rgba(0,0,0,.12);
    overflow: hidden;
  }
  .card--top-left  { left: 88px;  top: 152px; }
  .card--top-right { left: 670px; top: 152px; }
  .card--bottom    { left: 378px; top: 660px; }

  .brand-art {
    position: absolute;
    left: 24px; top: 46px;
    width: 176px; height: 112px;
    border-radius: 6px;
    background: linear-gradient(160deg, var(--navy) 0%, #4a6aa8 38%, #e9e9ef 52%, #c4353a 70%, var(--red-dark) 100%);
    opacity: .9;
  }
  .brand-name {
    position: absolute;
    left: 14px; top: 168px;
    width: 196px;
    text-align: center;
    font-family: "Alegreya", Georgia, serif;
    font-weight: 400;
    font-size: 17px;
    line-height: 18px;
    color: var(--ink);
  }

  .person {
    position: absolute;
    left: 220px; top: 62px;
    right: 8px;
  }
  .person__name {
    font-family: "Cinzel", "Times New Roman", serif;
    font-weight: 600;
    font-size: 17px;
    color: var(--navy);
    line-height: 22px;
    white-space: nowrap;
  }
  .person__role {
    font-size: 12.5px;
    color: var(--ink-soft);
    margin-top: 1px;
    white-space: nowrap;
  }
  .contact {
    list-style: none;
    position: absolute;
    left: 220px; top: 122px;
    font-size: 12px;
    line-height: 17px;
    color: var(--ink);
  }
  .contact li { display: flex; align-items: center; gap: 6px; white-space: nowrap; }
  .contact .icon { width: 10px; height: 10px; fill: var(--ink); color: var(--ink); flex: none; }
  .contact .address { margin-top: 3px; }

  .band-line {
    position: absolute;
    left: 0; bottom: 0;
    width: 200px; height: 6px;
    background: var(--blue-line);
  }
  .band {
    position: absolute;
    left: 194px; right: 0; bottom: 0;
    height: 34px;
    background: linear-gradient(90deg, var(--red-dark), var(--red));
    clip-path: polygon(14px 0, 100% 0, 100% 100%, 0 100%);
    color: var(--band-text);
    font-size: 12.5px;
    font-weight: 500;
    display: flex; align-items: center;
    padding-left: 44px;
  }
</style>
</head>
<body>
<svg width="0" height="0" style="position:absolute" aria-hidden="true">
  <defs>
    <symbol id="icon-phone" viewBox="0 0 10 10">
      <path d="M1 3.2C1 2 2.2 1.4 5 1.4S9 2 9 3.2V4H7V3.1H3V4H1z"/>
      <rect x="2.2" y="4.6" width="5.6" height="4.2" rx=".6"/>
    </symbol>
    <symbol id="icon-mail" viewBox="0 0 10 10">
      <path d="M0.5 2h9v6h-9z M1.5 3l3.5 2.6L8.5 3" stroke="#fbfbfa" stroke-width=".8"/>
    </symbol>
    <symbol id="icon-globe" viewBox="0 0 10 10">
      <circle cx="5" cy="5" r="4.3" fill="none" stroke="currentColor" stroke-width="1"/>
      <path d="M0.8 5h8.4M5 .8v8.4M2 2.6h6M2 7.4h6" fill="none" stroke="currentColor" stroke-width=".7"/>
    </symbol>
  </defs>
</svg>

<article class="card card--top-left">
  <div class="brand-art" role="img" aria-label="Brushed flag artwork in blue, white and red"></div>
  <div class="brand-name">Bramwell Ridge<br>Minerals</div>
  <div class="person">
    <h2 class="person__name">Maren Jo Hale</h2>
    <p class="person__role">Manager and Executive Assistant</p>
  </div>
  <ul class="contact">
    <li><svg class="icon"><use href="#icon-phone"/></svg>555-310-4827</li>
    <li><svg class="icon"><use href="#icon-mail"/></svg>maren@bramwellridgeminerals.com</li>
    <li><svg class="icon"><use href="#icon-globe"/></svg>www.bramwellridgeminerals.com</li>
    <li class="address">1420 Cedar Bend #210 Austin, TX 78701</li>
  </ul>
  <div class="band-line"></div>
  <div class="band">Bramwell Ridge Minerals</div>
</article>

<article class="card card--top-right">
  <div class="brand-art" role="img" aria-label="Brushed flag artwork in blue, white and red"></div>
  <div class="brand-name">Bramwell Ridge<br>Minerals</div>
  <div class="person">
    <h2 class="person__name">Cal T. Hoyer</h2>
    <p class="person__role">General Partner</p>
  </div>
  <ul class="contact">
    <li><svg class="icon"><use href="#icon-phone"/></svg>555-310-4861</li>
    <li><svg class="icon"><use href="#icon-mail"/></svg>cal@bramwellridgeminerals.com</li>
    <li><svg class="icon"><use href="#icon-globe"/></svg>www.bramwellridgeminerals.com</li>
    <li class="address">1420 Cedar Bend #210 Austin, TX 78701</li>
  </ul>
  <div class="band-line"></div>
  <div class="band">Bramwell Ridge Minerals</div>
</article>

<article class="card card--bottom">
  <div class="brand-art" role="img" aria-label="Brushed flag artwork in blue, white and red"></div>
  <div class="brand-name">Bramwell Ridge<br>Minerals</div>
  <div class="person">
    <h2 class="person__name">Nico Estrada</h2>
    <p class="person__role">Public Relations Manager</p>
  </div>
  <ul class="contact">
    <li><svg class="icon"><use href="#icon-phone"/></svg>555-620-3400</li>
    <li><svg class="icon"><use href="#icon-mail"/></svg>nico@bramwellridgeminerals.com</li>
    <li><svg class="icon"><use href="#icon-globe"/></svg>www.bramwellridgeminerals.com</li>
    <li class="address">1420 Cedar Bend #210 Austin, TX 78701</li>
  </ul>
  <div class="band-line"></div>
  <div class="band">Bramwell Ridge Minerals</div>
</article>
</body>
</html>
```